Website Homepage Design for New Cosmetic Line

Design the Homepage for the website based on a provided Wireframe. Assets have been be provided for the design, with the expectation that the designer will provide the creative flair. Along with the homepage design, a list of site fonts and colours will also be needed for internal pages (but no internal page designs required. )
Layout/wireframe is here: http://verano-plumcosmetics.com/layout/ (and also attached in files as PNG and PDF)
No need to follow the Layout exactly as far as spacing and font go, just make sure all elements are on the page, and look amazing!
My Client gave these sites for comparable in the industry:
https://www.quorvabeauty.com/
https://www.marisoltenderwoodglow.com/ (does not like video in header though)

Moving Down the Wireframe:
Header Logo - Use the Text only from the logo, not the Circle at the top here
Navigation - Copy these items
Hero Image: Use the image stated. Feel free to add some creativity over it, make sure that the lips and product are still visible, and also that the Text that is being overlaid can be easily read
Arm Swatch and Lip Swatches, make them pop!
Featured Products, 2 of the images are in RAW from the photographer - you may want to convert them to jpg. Feel free to adjust if needed, for sizing and brightness. If you want to crop the images from the backgrounds, you could do that too to allow for more consistency.
Reviews show the needed content as well.

Footer speaks for itself - use the Full Round Logo here.

All Assets are here: https://files.stashbarn.net/folders/8kQwLmZ2xR4tYp9VnHc3JdE6sUb7aGo?usp=sharing

The main assets are also attached in a zip file, but there are more in the above shared link for additional creativity/resources

• Unique and Beautiful Design
Clear Layout
Follow Best Practices in Design layout for development (eg based on 12 grid)
Please Use Google Fonts

```html
<!DOCTYPE html>
<html lang="en">
<head>
<meta charset="utf-8">
<title>Verano Plum Cosmetics — Home</title>
<link href="https://fonts.googleapis.com/css2?family=Poppins:wght@400;500;600;700&family=Playfair+Display:wght@400;700&display=swap" rel="stylesheet">
<style>
:root{
  --pink:#f6878a;
  --pink-deep:#ef6f74;
  --blush:#fdeeee;
  --mist:#ebe9e9;
  --ink:#1d1d1d;
  --grey:#777;
  --white:#fff;
}
*{box-sizing:border-box;margin:0;padding:0}
html,body{width:1200px;height:3236px;overflow:hidden}
body{position:relative;background:var(--white);font-family:'Poppins',sans-serif;color:var(--ink)}
.abs{position:absolute}
.btn{display:inline-block;background:var(--pink);color:var(--white);font-size:13px;font-weight:500;padding:11px 24px;border-radius:3px;white-space:nowrap}
.btn.sm{font-size:11px;padding:8px 18px}
p.body{font-size:13px;line-height:1.65;color:var(--grey)}

/* top bar */
.topbar{top:0;left:0;width:1200px;height:48px;background:var(--white)}
.topbar .contact{top:16px;font-size:11px;color:#444;display:flex;align-items:center;gap:6px}
.brand{left:0;width:1200px;top:10px;text-align:center;font-family:'Playfair Display',serif;font-size:20px;color:var(--ink)}
.socials{top:17px;right:150px;display:flex;gap:10px}
.socials span{width:12px;height:12px;border-radius:50%;background:#333;display:block}

/* nav */
.nav{top:48px;left:0;width:1200px;height:32px;background:var(--pink)}
.nav ul{position:absolute;left:160px;top:9px;display:flex;gap:38px;list-style:none;font-size:11px;color:var(--white)}
.search{position:absolute;left:600px;top:6px;width:180px;height:20px;background:var(--white);border-radius:2px;font-size:10px;color:#555;padding:3px 10px}
.nav .icons{position:absolute;left:1000px;top:7px;display:flex;gap:14px}

/* hero */
.hero{top:80px;left:0;width:1200px;height:520px;background:var(--mist)}
.hero h1{position:absolute;left:160px;top:190px;width:380px;font-size:34px;line-height:1.2;font-weight:700;white-space:nowrap}
.hero p.body{position:absolute;left:160px;top:286px;width:340px;font-size:12px;line-height:1.5}
.hero-cta{position:absolute;left:160px;top:380px}
.lipstick{left:556px;top:230px;width:64px;height:170px;background:linear-gradient(160deg,#f3a2b6,#e3557e 45%,#c9c9cc 60%,#8d8d92);border-radius:10px 10px 4px 4px}
.lips{left:660px;top:65px;width:380px;height:507px;border:6px solid var(--white);background:linear-gradient(180deg,#e9b2a9 0%,#d65a82 38%,#c74474 52%,#f2b7c4 70%,#e56e93 100%);box-shadow:0 6px 18px rgba(0,0,0,.12)}

/* mission */
.mission{top:600px;left:0;width:1200px;height:600px}
.frame{left:160px;top:135px;width:380px;height:310px;border:4px solid var(--pink)}
.portrait{left:190px;top:160px;width:320px;height:260px;background:linear-gradient(135deg,#f1f1f1,#9b9b9b 55%,#c0c0c0)}
.mission h2{position:absolute;left:620px;top:195px;font-family:'Playfair Display',serif;font-size:28px;font-weight:400}
.mission p.body{position:absolute;left:620px;top:245px;width:420px;font-size:12px}
.mission-cta{position:absolute;left:620px;top:340px}

/* by us for all */
.forall{top:1200px;left:0;width:1200px;height:740px;background:var(--blush)}
.forall h2{position:absolute;left:0;width:1200px;top:50px;text-align:center;font-family:'Playfair Display',serif;font-size:24px;font-weight:700}
.grid{left:160px;top:95px;width:885px;height:535px}
.tile-palette{left:0;top:0;width:290px;height:535px;background:linear-gradient(160deg,#3d2a2c,#c95b6c 40%,#2f2022 70%,#e08c97)}
.tile-new{left:20px;top:295px;width:140px;height:110px;background:rgba(20,20,20,.82);color:var(--white);font-family:'Playfair Display',serif;font-size:15px;text-align:center;padding:30px 10px;line-height:1.3}
.tile-offer{left:290px;top:0;width:310px;height:270px;background:var(--pink)}
.offer-card{left:310px;top:18px;width:270px;height:234px;border:2px solid rgba(255,255,255,.7);text-align:center;color:var(--white)}
.offer-card .lbl{font-family:'Playfair Display',serif;font-size:16px;margin-top:22px}
.offer-card .pct{font-size:60px;font-weight:500;line-height:1.2;margin-top:8px}
.offer-card .btn{background:var(--pink-deep);margin-top:12px}
.tile-shelf{left:290px;top:270px;width:310px;height:265px;background:linear-gradient(150deg,#5a3b3e,#e0788a 45%,#3b2a2c 80%)}
.tile-swatch{left:600px;top:0;width:285px;height:535px;background:linear-gradient(90deg,#d9b6a2,#c59a86 50%,#b8836f)}
.forall-cta{position:absolute;left:553px;top:660px}

/* trending */
.trending{top:1940px;left:0;width:1200px;height:640px}
.trending h2{position:absolute;left:0;width:1200px;top:50px;text-align:center;font-family:'Playfair Display',serif;font-size:24px;font-weight:700}
.tabs{left:0;width:1200px;top:110px;display:flex;justify-content:center;gap:22px;font-size:11px;font-weight:500}
.tabs span{padding:4px 12px}
.tabs .on{background:var(--pink);color:var(--white);border-radius:3px}
.cards{left:160px;top:150px;width:885px;display:flex;gap:16px}
.card{position:relative;width:209px;height:340px;background:var(--white);box-shadow:0 2px 12px rgba(0,0,0,.1);text-align:center}
.tag{position:absolute;left:0;top:14px;background:var(--pink);color:var(--white);font-size:11px;padding:3px 8px}
.was{position:absolute;right:16px;top:17px;font-size:11px;color:#aaa;text-decoration:line-through}
.bottle{width:34px;height:150px;margin:60px auto 0;background:linear-gradient(180deg,#1d1d1d 0 38%,#8f4d47 38%,#a25e57 100%);border-radius:3px}
.card h3{font-family:'Playfair Display',serif;font-weight:400;font-size:14px;margin-top:20px}
.stars{color:var(--pink);font-size:11px;letter-spacing:2px;margin-top:4px}
.card .btn{margin-top:14px}

/* reviews */
.reviews{top:2580px;left:0;width:1200px;height:380px;background:#f2eeee}
.reviews h2{position:absolute;left:0;width:1200px;top:50px;text-align:center;font-family:'Playfair Display',serif;font-size:24px;font-weight:400;letter-spacing:1px}
.quotes{left:140px;top:110px;width:920px;display:flex;justify-content:space-between}
.quote{width:280px}
.quote .box{position:relative;background:var(--white);padding:18px 22px 18px 42px;font-size:12px;line-height:1.55;color:#555;box-shadow:0 2px 10px rgba(0,0,0,.06)}
.quote .box::before{content:"\201C";position:absolute;left:12px;top:2px;font-family:'Playfair Display',serif;font-size:44px;color:#d4d4d4}
.who{display:flex;align-items:center;gap:12px;margin:24px 0 0 10px}
.avatar{width:46px;height:46px;border-radius:50%;background:linear-gradient(135deg,#e8c6b8,#9c7a6c)}
.who b{display:block;font-size:11px}
.who small{font-size:9px;color:#999}

/* footer */
.footer{top:2960px;left:0;width:1200px;height:276px;background:var(--pink);color:var(--white)}
.seal{left:180px;top:60px;width:130px;height:130px;border:2px solid rgba(255,255,255,.85);border-radius:50%;display:flex;align-items:center;justify-content:center;text-align:center;font-family:'Playfair Display',serif;font-size:14px;line-height:1.3}
.col h4{font-size:12px;font-weight:600;letter-spacing:1px;margin-bottom:10px}
.col p{font-size:11px;line-height:1.6;opacity:.9}
.foot-social{display:flex;gap:12px;margin-top:14px}
.foot-social span{width:14px;height:14px;border-radius:50%;background:var(--white);display:block}
.signup{display:flex;margin-top:14px}
.signup .field{width:130px;height:30px;background:var(--white);color:#999;font-size:10px;padding:8px 10px}
.signup .go{height:30px;background:var(--pink-deep);font-size:10px;padding:8px 12px}
.ghost{display:inline-block;margin-top:14px;border:1px solid var(--white);font-size:10px;padding:7px 16px;border-radius:2px}
.copy{right:130px;bottom:18px;font-size:9px;opacity:.85}
</style>
</head>
<body>

<header class="abs topbar">
  <div class="abs contact" style="left:160px">
    <svg width="12" height="10" viewBox="0 0 12 10"><rect x=".5" y=".5" width="11" height="9" fill="none" stroke="#333"/><path d="M.5 .5 6 5.5 11.5 .5" fill="none" stroke="#333"/></svg>
    hello@veranoplum.com
  </div>
  <div class="abs contact" style="left:360px">
    <svg width="11" height="11" viewBox="0 0 24 24"><path d="M6.6 10.8a15 15 0 0 0 6.6 6.6l2.2-2.2a1 1 0 0 1 1-.25 11.4 11.4 0 0 0 3.6.6 1 1 0 0 1 1 1V20a1 1 0 0 1-1 1A17 17 0 0 1 3 4a1 1 0 0 1 1-1h3.5a1 1 0 0 1 1 1c0 1.25.2 2.45.6 3.6a1 1 0 0 1-.25 1z" fill="#333"/></svg>
    1 (555) 010-2244
  </div>
  <div class="abs brand">Verano Plum Cosmetics</div>
  <div class="abs socials"><span></span><span></span><span></span><span></span><span></span></div>
</header>

<nav class="abs nav">
  <ul><li>Home</li><li>Skincare</li><li>Product</li><li>Services</li><li>Contact Us</li></ul>
  <div class="search">Search Product</div>
  <div class="icons">
    <svg width="18" height="18" viewBox="0 0 24 24"><circle cx="12" cy="12" r="9" fill="none" stroke="#fff" stroke-width="2"/><circle cx="12" cy="12" r="3" fill="#fff"/></svg>
    <svg width="18" height="18" viewBox="0 0 24 24"><circle cx="12" cy="8" r="4" fill="#fff"/><path d="M4 21a8 8 0 0 1 16 0z" fill="#fff"/></svg>
  </div>
</nav>

<section class="abs hero">
  <h1>Fully Canadian<br>Owned and Operate</h1>
  <p class="body">Lorem ipsum dolor sit amet consectetur adipisci elit, sed do eiusmod tempor incididunt.</p>
  <span class="btn hero-cta">Shop Now</span>
  <div class="abs lipstick" role="img" aria-label="Pink lipstick with silver case"></div>
  <div class="abs lips" role="img" aria-label="Close-up of pink glossy lips above a pink product tube"></div>
</section>

<section class="abs mission">
  <div class="abs frame"></div>
  <div class="abs portrait" role="img" aria-label="Black and white portrait of a model applying red lipstick"></div>
  <h2>Our Mission</h2>
  <p class="body">Lorem ipsum dolor sit amet, consectetur adipiscing elit, sed do eiusmod tempor incididunt ut labore et dolore magna aliqua. Quis ipsum suspendisse ultrices gravida. Risus commodo viverra maecenas accumsan lacus vel facilisis.</p>
  <span class="btn sm mission-cta">Shop Now</span>
</section>

<section class="abs forall">
  <h2>By Us For All</h2>
  <div class="abs grid">
    <div class="abs tile-palette" role="img" aria-label="Stacks of pink and red eyeshadow palettes"></div>
    <div class="abs tile-new">There's Nothing Like New</div>
    <div class="abs tile-offer"></div>
    <div class="abs offer-card">
      <div class="lbl">Cosmetic Product</div>
      <div class="pct">25%</div>
      <span class="btn sm">Shop Now</span>
    </div>
    <div class="abs tile-shelf" role="img" aria-label="Rows of makeup palettes on a display"></div>
    <div class="abs tile-swatch" role="img" aria-label="Lip colour swatches on an arm"></div>
  </div>
  <span class="btn sm forall-cta">Shop Now</span>
</section>

<section class="abs trending">
  <h2>Trending Products</h2>
  <div class="abs tabs"><span class="on">Cosmetics</span><span>Best Sellers</span><span>New Products</span></div>
  <div class="abs cards">
    <article class="card"><span class="tag">$14.00</span><span class="was">$18.00</span><div class="bottle" role="img" aria-label="Liquid lipstick bottle"></div><h3>Beauty Product</h3><div class="stars">★★★★★</div><span class="btn sm">Shop Now</span></article>
    <article class="card"><span class="tag">$14.00</span><span class="was">$18.00</span><div class="bottle" role="img" aria-label="Liquid lipstick bottle"></div><h3>Skin Care Product</h3><div class="stars">★★★★★</div><span class="btn sm">Shop Now</span></article>
    <article class="card"><span class="tag">$14.00</span><span class="was">$18.00</span><div class="bottle" role="img" aria-label="Liquid lipstick bottle"></div><h3>Supplements Product</h3><div class="stars">★★★★★</div><span class="btn sm">Shop Now</span></article>
    <article class="card"><span class="tag">$14.00</span><span class="was">$18.00</span><div class="bottle" role="img" aria-label="Liquid lipstick bottle"></div><h3>skin care products</h3><div class="stars">★★★★★</div><span class="btn sm">Shop Now</span></article>
  </div>
</section>

<section class="abs reviews">
  <h2>WHAT PEOPLE SAY ABOUT US</h2>
  <div class="abs quotes">
    <div class="quote"><div class="box">Lorem ipsum dolor sit amet, consectetur adipiscing elit, sed do eiusmod tempor incididunt ut labore et dolore magna aliqua. Quis ipsum suspendisse ultrices gravida. Accumsan</div>
      <div class="who"><div class="avatar" role="img" aria-label="Client photo"></div><div><b>MIRA SOLENNE</b><small>CLIENT</small><div class="stars">★★★★★</div></div></div></div>
    <div class="quote"><div class="box">Lorem ipsum dolor sit amet, consectetur adipiscing elit, sed do eiusmod tempor incididunt ut labore et dolore magna aliqua. Quis ipsum suspendisse ultrices gravida. Accumsan</div>
      <div class="who"><div class="avatar" role="img" aria-label="Client photo"></div><div><b>TESSA ORLIN</b><small>CLIENT</small><div class="stars">★★★★★</div></div></div></div>
    <div class="quote"><div class="box">Lorem ipsum dolor sit amet, consectetur adipiscing elit, sed do eiusmod tempor incididunt ut labore et dolore magna aliqua. Quis ipsum suspendisse ultrices gravida. Accumsan</div>
      <div class="who"><div class="avatar" role="img" aria-label="Client photo"></div><div><b>JUNO MARLOWE</b><small>CLIENT</small><div class="stars">★★★★★</div></div></div></div>
  </div>
</section>

<footer class="abs footer">
  <div class="abs seal">Verano Plum<br>Cosmetics</div>
  <div class="abs col" style="left:420px;top:70px;width:180px">
    <h4>CONNECT MORE</h4>
    <p>Lorem ipsum dolor sit amet consectetur adipiscing elit.</p>
    <div class="foot-social"><span></span><span></span><span></span><span></span></div>
  </div>
  <div class="abs col" style="left:650px;top:70px;width:220px">
    <h4>EMAIL UPDATE</h4>
    <p>Sign up for news, offers and new product drops.</p>
    <div class="signup"><div class="field">Enter your email</div><div class="go">SUBMIT</div></div>
  </div>
  <div class="abs col" style="left:920px;top:70px;width:160px">
    <h4>CONTACT US</h4>
    <p>Reach our team with any questions.</p>
    <span class="ghost">SEND US</span>
  </div>
  <div class="abs copy">© Verano Plum Cosmetics</div>
</footer>

</body>
</html>
```